Biz card for law firm
BH Lodestar Law, PLLC
Cutting-Edge
Marcus T. Delwyn
Registered Patent Attorney
3862 Millbrook Crest Lane
Suite 418
Raleigh, NC 27649
mtdelwyn@bhlodestarlaw.com
www.bhlodestarlaw.com
Bohr atomic model with BH Lodestar Law below

```html
<!DOCTYPE html>
<html lang="en">
<head>
<meta charset="utf-8">
<title>BH Lodestar Law, PLLC — Stationery</title>
<link href="https://fonts.googleapis.com/css2?family=Marcellus&family=Open+Sans:wght@400;600&display=swap" rel="stylesheet">
<style>
  :root {
    --navy: #0b2a7a;
    --blue: #1646b8;
    --sky: #4f7fe0;
    --paper: #ffffff;
    --ground: #eef0f3;
    --ink: #1b3a8c;
    --grey: #6b7280;
    --faint: #e3e8f3;
  }
  html, body { margin: 0; padding: 0; overflow: hidden; }
  body {
    width: 1200px; height: 936px; position: relative;
    background: var(--ground);
    font-family: "Open Sans", Arial, sans-serif;
  }
  .sheet { position: absolute; background: var(--paper); overflow: hidden; }
  .sheet svg.swoosh { position: absolute; inset: 0; width: 100%; height: 100%; }

  .brand { position: absolute; display: flex; align-items: center; gap: 10px;
    font-family: "Marcellus", Georgia, serif; color: var(--ink); white-space: nowrap; }
  .brand .mark { background: var(--blue); flex: none; }

  .letterhead { left: 182px; top: 63px; width: 395px; height: 549px; }
  .letterhead .brand { left: 26px; top: 30px; font-size: 22px; }
  .letterhead .brand .mark { width: 38px; height: 38px; }
  .letterhead .watermark { position: absolute; left: 150px; top: 245px; width: 95px; height: 70px;
    background: var(--faint); }
  .letterhead .contact { position: absolute; left: 26px; bottom: 22px; font-size: 7px;
    line-height: 11px; color: var(--grey); }

  .folder { left: 633px; top: 38px; width: 460px; height: 574px; }
  .folder .brand { left: 64px; top: 212px; font-size: 26px; gap: 12px; }
  .folder .brand .mark { width: 48px; height: 48px; }

  .card { left: 46px; width: 177px; height: 72px; }
  .card-front { top: 653px; }
  .card-front .brand { left: 10px; top: 9px; font-size: 9px; gap: 5px; }
  .card-front .brand .mark { width: 15px; height: 15px; }
  .card-front .person { position: absolute; right: 36px; top: 31px; font-size: 5px;
    line-height: 7px; color: var(--ink); text-align: right; }
  .card-front .details { position: absolute; left: 10px; bottom: 6px; font-size: 4.6px;
    line-height: 6px; color: var(--grey); }
  .card-back { top: 744px; }
  .card-back .texture { position: absolute; inset: 0;
    background: radial-gradient(circle at 55% 40%, var(--sky), var(--blue) 45%, var(--navy)); }
  .card-back .url { position: absolute; left: 0; right: 0; bottom: 8px; text-align: center;
    font-size: 5px; letter-spacing: 1px; color: #dbe6ff; }

  .envelope { top: 663px; width: 435px; height: 210px; }
  .envelope-front { left: 261px; }
  .envelope-front .brand { left: 18px; top: 14px; font-size: 20px; gap: 8px; }
  .envelope-front .brand .mark { width: 34px; height: 34px; }
  .envelope-back { left: 734px; width: 430px; }
  .envelope-back .url { position: absolute; left: 0; right: 0; top: 26px; text-align: center;
    font-size: 7px; letter-spacing: 2px; color: #dbe6ff; }
</style>
</head>
<body>
<svg width="0" height="0" style="position:absolute">
  <defs>
    <linearGradient id="band" x1="0" y1="0" x2="1" y2="0">
      <stop offset="0" stop-color="#0b2a7a"/>
      <stop offset="0.5" stop-color="#1646b8"/>
      <stop offset="1" stop-color="#0b2a7a"/>
    </linearGradient>
  </defs>
</svg>

<section class="sheet letterhead">
  <svg class="swoosh" viewBox="0 0 395 549" preserveAspectRatio="none">
    <path d="M300 0 C370 130 395 300 395 470 L395 0 Z" fill="url(#band)"/>
    <path d="M262 0 C335 140 362 320 350 549" fill="none" stroke="#1646b8" stroke-width="3"/>
  </svg>
  <div class="brand"><span class="mark"></span>BH Lodestar Law</div>
  <div class="watermark"></div>
  <div class="contact">
    3862 Millbrook Crest Lane<br>Suite 418<br>Raleigh, NC 27649<br>
    Tel 919.555.0142<br>Fax 919.555.0143<br>mtdelwyn@bhlodestarlaw.com<br>www.bhlodestarlaw.com
  </div>
</section>

<section class="sheet folder">
  <svg class="swoosh" viewBox="0 0 460 574" preserveAspectRatio="none">
    <path d="M330 0 C430 150 440 380 370 574 L460 574 L460 0 Z" fill="url(#band)"/>
    <path d="M285 0 C390 160 405 390 330 574" fill="none" stroke="#1646b8" stroke-width="4"/>
  </svg>
  <div class="brand"><span class="mark"></span>BH Lodestar Law</div>
</section>

<section class="sheet card card-front">
  <svg class="swoosh" viewBox="0 0 177 72" preserveAspectRatio="none">
    <path d="M150 0 C172 20 177 45 168 72 L177 72 L177 0 Z" fill="url(#band)"/>
  </svg>
  <div class="brand"><span class="mark"></span>BH Lodestar Law</div>
  <div class="person">Marcus T. Delwyn<br>Registered Patent Attorney</div>
  <div class="details">3862 Millbrook Crest Lane, Suite 418, Raleigh, NC 27649<br>mtdelwyn@bhlodestarlaw.com</div>
</section>

<section class="sheet card card-back">
  <div class="texture" role="img" aria-label="Deep blue textured card back"></div>
  <div class="url">www.bhlodestarlaw.com</div>
</section>

<section class="sheet envelope envelope-front">
  <svg class="swoosh" viewBox="0 0 435 210" preserveAspectRatio="none">
    <path d="M385 0 C420 60 430 140 410 210 L435 210 L435 0 Z" fill="url(#band)"/>
    <path d="M360 0 C398 70 404 150 385 210" fill="none" stroke="#1646b8" stroke-width="3"/>
  </svg>
  <div class="brand"><span class="mark"></span>BH Lodestar Law</div>
</section>

<section class="sheet envelope envelope-back">
  <svg class="swoosh" viewBox="0 0 430 210" preserveAspectRatio="none">
    <path d="M0 0 L430 0 L430 60 C300 95 130 95 0 60 Z" fill="url(#band)"/>
  </svg>
  <div class="url">www.bhlodestarlaw.com</div>
</section>
</body>
</html>
```